Broschüre für unsere Firma
Zielgruppe
Wäscherei Kranzbeck / Textilservice
Geschäftskunden
Logos etc. In OneDrive/ Dropbox
https://ablage-beispiel.de/f/s!XkrTmWq7PzvoNeFgHsYa4Lc92_p
Wir wollen gerne eine 4 seitige Broschüre erstellen lassen, um unsere Firma vorzustellen.
Insbesondere der Service
Berufsbekleidung
Hygiene Gardienenwäsche Service
Hotelmietwäsche
Mitbewerb
http://www.wäscherei-gollwitz.de/index.php/ct-menu-item-17/ct-menu-item-25
http://www.tuch-morgen.ch/download
Im Anhang finden Sie Bilder Logo und Flyers welche wir mal selbst gemacht haben!
Datein sind im OneDrive
Aufgabenstellung

```html
<!DOCTYPE html>
<html lang="de">
<head>
<meta charset="utf-8">
<title>Wäscherei Kranzbeck – Broschüre</title>
<link rel="stylesheet" href="https://fonts.googleapis.com/css2?family=Marcellus&family=Open+Sans:wght@400;700&display=swap">
<style>
  :root {
    --navy: #17336a;
    --navy-deep: #0f2450;
    --green: #8fb21d;
    --green-dark: #6f9a1a;
    --lime: #c8d81e;
    --blue: #1591d0;
    --lavender: #c9c7e2;
    --plum: #2b1f5c;
    --gold: #f2cf6a;
    --white: #ffffff;
    --stage: #e7e7e9;
    --serif: "Marcellus", Georgia, serif;
    --sans: "Open Sans", Arial, sans-serif;
  }
  * { box-sizing: border-box; margin: 0; padding: 0; }
  html, body { width: 1200px; height: 900px; overflow: hidden; background: var(--stage); }
  .canvas { position: relative; width: 1200px; height: 900px; }

  .page-art { position: absolute; inset: 0; width: 100%; height: 100%; display: block; }

  /* Cover */
  .cover { position: absolute; left: 310px; top: 28px; width: 580px; height: 410px; overflow: hidden; box-shadow: 0 6px 18px rgba(0,0,0,.18); }
  .cover-brand { position: absolute; left: 22px; top: 270px; display: flex; align-items: center; gap: 8px; white-space: nowrap; }
  .brand-dot { width: 20px; height: 20px; border-radius: 50%; background: var(--navy); flex: none; }
  .brand-name { font-family: var(--sans); font-weight: 700; font-size: 16px; color: var(--navy); }
  .brand-tagline { position: absolute; left: 50px; top: 296px; font-family: var(--sans); font-size: 8px; color: var(--navy); white-space: nowrap; }
  .cover-url { position: absolute; left: 22px; top: 340px; font-family: var(--sans); font-weight: 700; font-size: 12px; color: var(--navy-deep); white-space: nowrap; }
  .cover-claim { position: absolute; right: 34px; top: 338px; text-align: right; font-family: var(--serif); font-size: 15px; line-height: 1.25; color: var(--white); letter-spacing: .04em; }

  /* Inside spread */
  .spread { position: absolute; left: 20px; top: 468px; width: 1160px; height: 410px; overflow: hidden; box-shadow: 0 6px 18px rgba(0,0,0,.18); }
  .about-kicker { position: absolute; left: 40px; top: 28px; font-family: var(--serif); font-size: 18px; color: var(--white); letter-spacing: .03em; }
  .about-heading { position: absolute; left: 40px; top: 54px; width: 300px; font-family: var(--serif); font-size: 22px; line-height: 1.15; color: var(--green); }
  .about-rule { position: absolute; left: 40px; top: 112px; width: 270px; height: 1px; background: var(--blue); }
  .about-body { position: absolute; left: 40px; top: 124px; width: 280px; font-family: var(--sans); font-size: 11px; line-height: 1.55; color: #d6dcf0; }

  .service-title { position: absolute; font-family: var(--serif); font-size: 15px; color: var(--gold); line-height: 1.15; }
  .service-text { position: absolute; font-family: var(--sans); font-size: 10px; line-height: 1.5; color: #ece9f5; }

  .workwear-title { left: 395px; top: 222px; }
  .workwear-text { left: 395px; top: 244px; width: 165px; }
  .curtain-title { left: 640px; top: 196px; width: 200px; text-align: center; }
  .curtain-text { left: 650px; top: 240px; width: 180px; }
  .hotel-title { left: 930px; top: 196px; }
  .hotel-text { left: 925px; top: 222px; width: 210px; }
</style>
</head>
<body>
<main class="canvas">

  <section class="cover" aria-label="Titelseite">
    <svg class="page-art" viewBox="0 0 580 410" preserveAspectRatio="none">
      <defs>
        <linearGradient id="laundryTones" x1="0" x2="1" y1="0" y2="0">
          <stop offset="0" stop-color="#c8322a"/>
          <stop offset=".45" stop-color="#b02a24"/>
          <stop offset=".55" stop-color="#d8c34a"/>
          <stop offset="1" stop-color="#a9a04a"/>
        </linearGradient>
      </defs>
      <rect width="580" height="410" fill="var(--navy)"/>
      <polygon points="0,0 315,0 315,20 0,20" fill="var(--green-dark)"/>
      <polygon points="315,0 580,0 580,20 315,20" fill="#0c1d45"/>
      <polygon points="60,55 75,42 95,42 105,55 95,68 75,68" fill="#8a8a3a" opacity=".7"/>
      <polygon points="40,110 60,78 100,78 120,110 100,142 60,142" fill="#1d5b9b" opacity=".8"/>
      <polygon points="60,195 78,168 112,168 130,195 112,222 78,222" fill="#6a74a8" opacity=".6"/>
      <polygon points="505,40 515,25 535,25 545,40 535,55 515,55" fill="#1d5b9b" opacity=".8"/>
      <polygon points="470,255 495,215 545,215 570,255 545,295 495,295" fill="#24427f" opacity=".8"/>
      <polygon points="140,144 200,40 425,40 478,144 425,248 200,248" fill="#000"/>
      <polygon points="152,144 208,48 418,48 466,144 418,240 208,240" fill="url(#laundryTones)" role="img" aria-label="Foto: Reihe farbiger Waschmaschinen im Waschsalon"/>
      <polygon points="440,48 580,40 575,150 500,150" fill="var(--green)"/>
      <polygon points="385,48 440,48 505,150 440,250 385,250 448,150" fill="var(--blue)"/>
      <polygon points="0,252 250,252 310,410 0,410" fill="var(--lavender)"/>
    </svg>
    <div class="cover-brand"><span class="brand-dot"></span><span class="brand-name">Wäscherei Kranzbeck</span></div>
    <p class="brand-tagline">Textilservice für Geschäftskunden</p>
    <p class="cover-url">www.waescherei-kranzbeck.de</p>
    <p class="cover-claim">WO QUALITÄT<br>BESTIMMEND IST</p>
  </section>

  <section class="spread" aria-label="Innenseiten">
    <svg class="page-art" viewBox="0 0 1160 410" preserveAspectRatio="none">
      <defs>
        <linearGradient id="greenPanel" x1="0" x2="1" y1="1" y2="0">
          <stop offset="0" stop-color="var(--green-dark)"/>
          <stop offset="1" stop-color="#a8c41f"/>
        </linearGradient>
      </defs>
      <rect width="580" height="410" fill="var(--navy)"/>
      <rect x="580" width="320" height="410" fill="url(#greenPanel)"/>
      <rect x="894" width="8" height="410" fill="var(--lavender)"/>
      <rect x="902" width="258" height="410" fill="var(--navy)"/>
      <line x1="580" y1="0" x2="580" y2="410" stroke="#000" stroke-opacity=".15"/>

      <polygon points="420,130 435,105 465,105 480,130 465,155 435,155" fill="var(--blue)" opacity=".8"/>
      <polygon points="380,190 390,175 410,175 420,190 410,205 390,205" fill="var(--blue)" opacity=".8"/>
      <polygon points="240,330 262,292 306,292 328,330 306,368 262,368" fill="#6a74a8" opacity=".6"/>
      <polygon points="340,300 405,187 535,187 600,300 535,413 405,413" fill="var(--plum)" opacity=".88"/>
      <polygon points="600,300 670,179 810,179 880,300 810,421 670,421" fill="#4d5f18" opacity=".75"/>
      <polygon points="890,300 955,187 1085,187 1150,300 1085,413 955,413" fill="var(--navy-deep)" opacity=".7"/>
      <polygon points="590,360 615,318 665,318 690,360 665,402 615,402" fill="var(--lime)" opacity=".8"/>
      <polygon points="610,120 630,88 665,88 680,120 665,150 630,150" fill="var(--lime)" opacity=".6"/>
      <polygon points="820,120 830,105 850,105 860,120 850,135 830,135" fill="#d6e48a" opacity=".7"/>
      <polygon points="830,170 842,150 862,150 874,170 862,190 842,190" fill="#1aa39a" opacity=".9"/>
      <polygon points="1110,40 1120,25 1140,25 1150,40 1140,55 1120,55" fill="var(--blue)" opacity=".9"/>
      <polygon points="1075,40 1083,28 1100,28 1108,40 1100,52 1083,52" fill="#6a74a8" opacity=".8"/>
      <polygon points="1080,385 1090,368 1110,368 1120,385 1110,402 1090,402" fill="#6a74a8" opacity=".8"/>

      <polygon points="520,140 550,88 610,88 640,140 610,192 550,192" fill="#dfe8e2" stroke="var(--white)" stroke-width="3" role="img" aria-label="Foto: Arzt in weißem Kittel"/>
      <polygon points="675,110 707.5,53.7 772.5,53.7 805,110 772.5,166.3 707.5,166.3" fill="#e9d8cf" stroke="var(--white)" stroke-width="3" role="img" aria-label="Foto: Zimmermädchen beim Bettenmachen"/>
      <polygon points="955,110 987.5,53.7 1052.5,53.7 1085,110 1052.5,166.3 987.5,166.3" fill="#c9414a" stroke="var(--white)" stroke-width="3" role="img" aria-label="Foto: Mitarbeiterin in roter Dienstkleidung in der Wäscherei"/>
    </svg>

    <h2 class="about-kicker">ÜBER UNS</h2>
    <h3 class="about-heading">Testen Sie uns und überzeugen Sie sich</h3>
    <span class="about-rule"></span>
    <p class="about-body">Seit vielen Jahren steht unsere Wäscherei für saubere Arbeit, kurze Wege und einen persönlichen Ansprechpartner. Wir pflegen Textilien für Praxen, Betriebe und Hotels mit moderner Technik und viel Sorgfalt. Abholung und Lieferung planen wir ganz nach Ihrem Rhythmus. Testen Sie unseren Service unverbindlich und lernen Sie uns kennen.</p>

    <h3 class="service-title workwear-title">Berufsbekleidung</h3>
    <p class="service-text workwear-text">Wenn es um Ihre Arbeitskleidung geht, sind Sie bei uns richtig. Wir reinigen, prüfen und reparieren Ihre Berufsbekleidung und stellen sie pünktlich zur Verfügung.</p>

    <h3 class="service-title curtain-title">Hygiene Gardienen-<br>wäsche Service</h3>
    <p class="service-text curtain-text">Gardinen waschen wir schonend und hygienisch sauber. Auf Wunsch nehmen wir sie ab, reinigen sie und hängen sie wieder fachgerecht auf.</p>

    <h3 class="service-title hotel-title">Hotelmietwäsche</h3>
    <p class="service-text hotel-text">In Ihrem Hotel erwartet Ihre Gäste exklusives Ambiente, eine gute Küche und eine herzliche Atmosphäre. Gerne unterstützen wir Sie hier mit unseren Dienstleistungen aus der hygienezertifizierten Wäscherei.</p>
  </section>

</main>
</body>
</html>
```